Stationery Required - Own Logo provided

Hi,

We are a retail company called 'Copperfinch Trading Limited' based in the UK and would like some corporate stationery designed.

We have provided our Logo which we would like to use (Its attached to this brief)...

The designs must be orginal, professional, stylish and interesting!

Target Market(s)

We will use this stationery to communicate with our wholesale suppliers and employees, so it must have a 'professional' feel about it.

Industry/Entity Type

It Company

Requirements
Must have
• Must be professional, corporate, stylish and not to 'fussy'. we require ... Business card design, a4 letter, compliment slip. All designs must be supplied in a format where the text (address/telephone numbers etc..) can be edited, as we have alot of staff and operate out of several different premises.
Nice to have
• I would like a windows backround picture file supplied as well so we can integrate that onto our computer systems.

```html
<!DOCTYPE html>
<html lang="en">
<head>
<meta charset="utf-8">
<title>Copperfinch Trading Limited – Business Cards</title>
<link rel="stylesheet" href="https://fonts.googleapis.com/css2?family=Arimo:wght@400;700&family=Cormorant+Garamond:wght@500&display=swap">
<style>
  :root {
    --green-dark: #3f6b2c;
    --green-mid: #6aa437;
    --green-light: #9cca55;
    --green-pale: #cfe59a;
    --ink: #1e1e1e;
    --white: #ffffff;
    --page: #eeeeea;
  }
  * { margin: 0; padding: 0; box-sizing: border-box; }
  html, body { width: 1200px; height: 900px; overflow: hidden; }
  body {
    background: var(--page);
    font-family: "Arimo", Arial, sans-serif;
    color: var(--ink);
    position: relative;
  }
  .card {
    position: absolute;
    width: 412px;
    height: 236px;
    background: var(--white);
    box-shadow: 0 2px 6px rgba(0,0,0,.25);
    overflow: hidden;
  }
  .card svg.card-art { position: absolute; inset: 0; width: 100%; height: 100%; }
  .card--front-a { left: 20px; top: 25px; }
  .card--front-b { left: 20px; top: 310px; }
  .card--back { left: 20px; top: 590px; }
  .card--brand {
    left: 602px; top: 25px; width: 416px;
    background: linear-gradient(to bottom, var(--green-light) 0%, var(--green-pale) 40%, #8fbf52 68%, var(--green-dark) 100%);
  }

  .holder-name {
    position: absolute; left: 50px; top: 62px;
    font-family: "Cormorant Garamond", Georgia, serif;
    font-weight: 500; font-size: 23px; color: var(--green-mid);
  }
  .holder-role {
    position: absolute; left: 70px; top: 93px;
    font-size: 9px; color: var(--ink);
  }
  .divider {
    position: absolute; left: 248px; top: 32px;
    width: 3px; height: 176px; background: var(--green-dark);
  }
  .contact {
    position: absolute; left: 266px; top: 66px;
    font-size: 9.5px; line-height: 14.5px; color: var(--ink);
    list-style: none;
  }
  .contact li.tight { line-height: 11px; }
  .contact .label { color: var(--green-mid); font-weight: 700; }
  .company-mark {
    position: absolute; left: 22px; top: 176px;
    font-size: 11px; font-weight: 700; color: var(--green-dark);
  }
  .brand-block {
    position: absolute; left: 0; right: 0; top: 98px;
    text-align: center; font-size: 26px; font-weight: 700;
    color: var(--green-dark);
  }
  .back-block {
    position: absolute; left: 0; right: 0; top: 80px; text-align: center;
  }
  .back-block .company {
    font-size: 26px; font-weight: 700; color: var(--green-dark);
  }
  .back-block .web {
    margin-top: 14px; font-size: 15px; font-weight: 700;
    letter-spacing: 1px; color: var(--ink);
  }
  .side-label {
    position: absolute; font-size: 24px; font-weight: 700;
    letter-spacing: 3px; color: var(--ink);
  }
</style>
</head>
<body>

<svg width="0" height="0" style="position:absolute">
  <defs>
    <linearGradient id="bar-top" x1="0" x2="1">
      <stop offset="0" stop-color="#3f6b2c"/>
      <stop offset=".55" stop-color="#7fae4a"/>
      <stop offset=".75" stop-color="#f2f2f2"/>
      <stop offset=".85" stop-color="#6aa437"/>
      <stop offset="1" stop-color="#3f6b2c"/>
    </linearGradient>
    <linearGradient id="bar-bottom" x1="0" x2="1">
      <stop offset="0" stop-color="#9cca55"/>
      <stop offset=".55" stop-color="#7fae4a"/>
      <stop offset=".62" stop-color="#f4f4f4"/>
      <stop offset=".8" stop-color="#9a9a9a"/>
      <stop offset="1" stop-color="#4c7a32"/>
    </linearGradient>
    <linearGradient id="side-panel" x1="0" y1="0" x2="0" y2="1">
      <stop offset="0" stop-color="#4c8a3a"/>
      <stop offset=".5" stop-color="#9cca55"/>
      <stop offset="1" stop-color="#3f6b2c"/>
    </linearGradient>
    <linearGradient id="wave-fill" x1="0" y1="0" x2="0" y2="1">
      <stop offset="0" stop-color="#9cca55"/>
      <stop offset="1" stop-color="#6aa437"/>
    </linearGradient>
    <linearGradient id="back-bg" x1="0" y1="0" x2="0" y2="1">
      <stop offset="0" stop-color="#9cca55"/>
      <stop offset=".3" stop-color="#ffffff"/>
      <stop offset=".72" stop-color="#ffffff"/>
      <stop offset="1" stop-color="#3f6b2c"/>
    </linearGradient>
    <clipPath id="white-panel">
      <path d="M0 22 H350 Q398 22 398 70 V172 Q398 220 350 220 H0 Z"/>
    </clipPath>
    <symbol id="front-art" viewBox="0 0 412 236">
      <rect width="412" height="236" fill="url(#side-panel)"/>
      <path d="M0 22 H350 Q398 22 398 70 V172 Q398 220 350 220 H0 Z" fill="#ffffff"/>
      <g clip-path="url(#white-panel)">
        <path d="M0 124 C70 128 150 170 230 200 C280 218 330 222 370 212 L400 236 H0 Z" fill="url(#wave-fill)"/>
        <path d="M0 124 C70 128 150 170 230 200 C280 218 330 222 370 212" fill="none" stroke="#3f6b2c" stroke-width="5"/>
      </g>
      <rect x="0" y="0" width="412" height="14" fill="url(#bar-top)"/>
      <rect x="0" y="224" width="412" height="12" fill="url(#bar-bottom)"/>
    </symbol>
    <symbol id="front-art-b" viewBox="0 0 412 236">
      <rect width="412" height="236" fill="url(#side-panel)"/>
      <path d="M0 22 H350 Q398 22 398 70 V172 Q398 220 350 220 H0 Z" fill="#ffffff"/>
      <rect x="0" y="0" width="412" height="14" fill="url(#bar-top)"/>
      <rect x="0" y="220" width="412" height="16" fill="url(#bar-bottom)"/>
    </symbol>
  </defs>
</svg>

<section class="card card--front-a" aria-label="Business card front">
  <svg class="card-art" viewBox="0 0 412 236" aria-hidden="true"><use href="#front-art"/></svg>
  <div class="holder-name">Martin Keller</div>
  <div class="holder-role">Company Director</div>
  <div class="divider"></div>
  <ul class="contact">
    <li>17 Harbour View Lane</li>
    <li>Ballyhalbert</li>
    <li>County Antrim</li>
    <li>BT22 4QX</li>
    <li class="tight"><span class="label">Tel:</span> 07700900417</li>
    <li class="tight"><span class="label">Email:</span> info@copperfinch.uk</li>
    <li class="tight">www.copperfinch.co.uk</li>
  </ul>
</section>

<section class="card card--brand" role="img" aria-label="Green gradient background with decorative wave pattern behind the company name">
  <div class="brand-block">Copperfinch Trading Limited</div>
</section>

<div class="side-label" style="left:442px; top:180px;">Front</div>

<section class="card card--front-b" aria-label="Business card front with company name">
  <svg class="card-art" viewBox="0 0 412 236" aria-hidden="true"><use href="#front-art-b"/></svg>
  <div class="holder-name">Martin Keller</div>
  <div class="holder-role">Company Director</div>
  <div class="divider"></div>
  <ul class="contact">
    <li>17 Harbour View Lane</li>
    <li>Ballyhalbert</li>
    <li>County Antrim</li>
    <li>BT22 4QX</li>
    <li class="tight"><span class="label">Tel:</span> 07700900417</li>
    <li class="tight"><span class="label">Email:</span> info@copperfinch.uk</li>
    <li class="tight">www.copperfinch.co.uk</li>
  </ul>
  <div class="company-mark">Copperfinch Trading Limited</div>
</section>

<div class="side-label" style="left:447px; top:430px;">Front</div>

<section class="card card--back" aria-label="Business card back">
  <svg class="card-art" viewBox="0 0 412 236" preserveAspectRatio="none" aria-hidden="true">
    <rect width="412" height="236" fill="url(#back-bg)"/>
  </svg>
  <div class="back-block">
    <div class="company">Copperfinch Trading Limited</div>
    <div class="web">www.copperfinch.co.uk</div>
  </div>
</section>

<div class="side-label" style="left:445px; top:653px;">Back</div>

</body>
</html>
```